tovrin company need business card, envelope and letterhead design

Check on the attached file wherein you can find our logo and information about the company
Business card will double sided English version and Arabic version

Industry/Entity Type

Business

Requirements
Must have
• include the design also for the letterhead and envelop
Nice to have

```html
<!DOCTYPE html>
<html lang="en">
<head>
<meta charset="utf-8">
<title>Tovrin business card</title>
<link rel="stylesheet" href="https://fonts.googleapis.com/css2?family=Open+Sans:wght@400;600;700&display=swap">
<style>
  :root {
    --backdrop: #e4e4e4;
    --brand-blue: #1476bd;
    --ink-blue: #1a72b6;
    --ink-grey: #767676;
    --card-white: #f7f7f7;
    --icon-grey: #8a8a8a;
  }
  * { margin: 0; padding: 0; box-sizing: border-box; }
  html, body { width: 1200px; height: 576px; overflow: hidden; }
  body {
    background: var(--backdrop);
    font-family: "Open Sans", Arial, sans-serif;
    position: relative;
  }
  .card {
    position: absolute;
    width: 493px;
    height: 270px;
    border-radius: 11px;
    overflow: hidden;
  }
  .card-front { left: 78px; top: 132px; background: var(--brand-blue); }
  .card-back { left: 603px; top: 134px; background: var(--card-white); }

  .wordmark {
    position: absolute;
    display: flex;
    align-items: center;
    font-weight: 700;
    line-height: 1;
  }
  .wordmark-square { display: block; flex: none; }
  .card-front .wordmark {
    left: 42px; top: 80px;
    color: #ffffff;
    font-size: 46px;
    letter-spacing: 9px;
    gap: 22px;
  }
  .card-front .wordmark-square { width: 80px; height: 80px; background: #ffffff; }
  .card-back .wordmark {
    left: 230px; top: 182px;
    color: var(--ink-blue);
    font-size: 28px;
    letter-spacing: 6px;
    gap: 12px;
  }
  .card-back .wordmark-square { width: 48px; height: 48px; background: var(--ink-blue); }

  .holder-name {
    position: absolute; left: 18px; top: 36px;
    color: var(--ink-blue); font-size: 15px; font-weight: 600; line-height: 20px;
  }
  .holder-title {
    position: absolute; left: 18px; top: 56px;
    color: var(--ink-grey); font-size: 10px; line-height: 14px;
  }
  .contact-line {
    position: absolute; left: 18px;
    display: flex; align-items: center; gap: 6px;
    color: var(--ink-blue); font-size: 9.5px; line-height: 12px;
  }
  .contact-line svg { width: 11px; height: 11px; fill: none; stroke: var(--icon-grey); stroke-width: 1.4; }
  .address {
    position: absolute; left: 18px;
    color: var(--ink-blue); font-size: 9px; font-weight: 600; line-height: 10px;
  }
</style>
</head>
<body>
  <section class="card card-front" aria-label="Card front">
    <div class="wordmark"><span class="wordmark-square"></span>TOVRIN</div>
  </section>

  <section class="card card-back" aria-label="Card back">
    <h1 class="holder-name">Fahad Bin Omar Al Rashidi</h1>
    <p class="holder-title">General Manager</p>

    <p class="contact-line" style="top:76px">
      <svg viewBox="0 0 12 12"><rect x="3" y="0.8" width="6" height="10.4" rx="1"/></svg>966 555 310 482
    </p>
    <p class="contact-line" style="top:178px">
      <svg viewBox="0 0 12 12"><circle cx="6" cy="6" r="5"/><path d="M4 3.5 L5 5 L4.5 5.8 Q5.5 7.3 6.5 7.6 L7.2 7 L8.6 8"/></svg>011 4720 356
    </p>
    <p class="contact-line" style="top:195px">
      <svg viewBox="0 0 12 12"><rect x="1.5" y="4.5" width="9" height="6.5" rx="1"/><rect x="3.5" y="1" width="5" height="3.5"/></svg>011 4720 357
    </p>
    <p class="contact-line" style="top:210px">
      <svg viewBox="0 0 12 12"><rect x="1" y="2.5" width="10" height="7"/><path d="M1 2.5 L6 6.5 L11 2.5"/></svg>tovrin.sa@mail.com
    </p>
    <p class="address" style="top:230px">Khalid Bin Waleed Road<br>Al Nakheel- P.O. Box 4213-11562</p>

    <div class="wordmark"><span class="wordmark-square"></span>TOVRIN</div>
  </section>
</body>
</html>
```